7 Vex Label

Design a label for 7 Vex styling gels. The logo is attached. The color is C=100, M=100, Y=0, K=0. The 16 oz. jar is also attached.

Updates

Attention all designers,

The old logo has been deleted.  I have uploaded a new logo for this project.  Can you please update your design with the NEW LOGO?
thank you,
Rob

Target Market(s)

Multicultural

Requirements
Must have
• you must used the logo attached.

text to be included on the jar:

Used by Professionals
Maximum Hold
Alcohol Free
NO FLAKING

16 oz.

As far as label size, use the jar photo, and fit the design on it.

```html
<!DOCTYPE html>
<html lang="en">
<head>
<meta charset="utf-8">
<title>7 Vex Styling Gel Label</title>
<link rel="stylesheet" href="https://fonts.googleapis.com/css2?family=Josefin+Sans:wght@300&family=Tinos:wght@400;700&display=swap">
<style>
  :root {
    --page-bg: #f3f3f3;
    --label-bg: #7fd6e0;
    --label-shadow: rgba(0, 0, 0, 0.18);
    --band-deep: #17a9c4;
    --band-mid: #36c6da;
    --band-light: #8fe6ee;
    --band-frame: #ffffff;
    --badge-fill: #cdeaf7;
    --brand-ink: #3d3a92;
    --title-ink: #2f2f36;
    --copy-ink: #3b2a45;
  }
  * { margin: 0; padding: 0; box-sizing: border-box; }
  html, body {
    width: 1200px;
    height: 800px;
    overflow: hidden;
  }
  body {
    background: radial-gradient(ellipse at center, #ffffff 0%, var(--page-bg) 75%);
    position: relative;
    font-family: "Tinos", "Times New Roman", serif;
  }
  .label {
    position: absolute;
    left: 268px;
    top: 70px;
    width: 662px;
    height: 660px;
    background: var(--label-bg);
    box-shadow: -4px 4px 3px var(--label-shadow);
    overflow: hidden;
  }
  .pattern-band {
    position: absolute;
    left: 17px;
    top: 153px;
    width: 630px;
    height: 333px;
    border: 2px solid var(--band-frame);
    background:
      radial-gradient(circle at 22% 30%, var(--band-light) 0%, transparent 30%),
      radial-gradient(circle at 78% 70%, var(--band-light) 0%, transparent 35%),
      radial-gradient(circle at 45% 60%, rgba(255,255,255,0.35) 0%, transparent 40%),
      linear-gradient(135deg, var(--band-mid) 0%, var(--band-deep) 50%, var(--band-mid) 100%);
  }
  .brand-badge {
    position: absolute;
    left: 220px;
    top: 40px;
    width: 224px;
    height: 224px;
    border-radius: 50%;
    background: var(--badge-fill);
    border: 2px solid var(--band-frame);
    display: flex;
    align-items: center;
    justify-content: center;
  }
  .brand-name {
    font-family: "Tinos", "Times New Roman", serif;
    font-weight: 700;
    font-size: 64px;
    color: var(--brand-ink);
    letter-spacing: 2px;
  }
  .product-title {
    position: absolute;
    left: 0;
    width: 662px;
    top: 314px;
    text-align: center;
    font-family: "Josefin Sans", "Helvetica", sans-serif;
    font-weight: 300;
    font-size: 124px;
    line-height: 1;
    color: var(--title-ink);
    letter-spacing: -2px;
    word-spacing: -18px;
    white-space: nowrap;
    transform: scaleX(0.7);
    transform-origin: center top;
  }
  .claims {
    position: absolute;
    left: 0;
    width: 662px;
    top: 525px;
    list-style: none;
    text-align: center;
    color: var(--copy-ink);
    font-size: 29px;
    line-height: 31px;
  }
  .net-weight {
    position: absolute;
    right: 12px;
    top: 611px;
    color: var(--copy-ink);
    font-size: 39px;
    line-height: 1;
    letter-spacing: 1px;
  }
</style>
</head>
<body>
  <main class="label">
    <div class="pattern-band" role="img" aria-label="Decorative pattern of flowing white lines and overlapping circles in aqua and teal tones"></div>
    <div class="brand-badge">
      <span class="brand-name">7 Vex</span>
    </div>
    <h1 class="product-title">STYLING GEL</h1>
    <ul class="claims">
      <li>Used by Professionals</li>
      <li>Maximum Hold</li>
      <li>Alcohol Free</li>
      <li>NO FLAKING</li>
    </ul>
    <p class="net-weight">16 oz.</p>
  </main>
</body>
</html>
```